R Dawson Naturopathy

Australian naturopath needs a business web page

Target Market(s)

adults both female and male, parents of children of all ages. Who value health.

Requirements
Must have
• request an appointment
contact
Pelo/Quintpay/Harborline Charge/TAPNET welcome signage
Should not have
• black and grey backgrounds
boring fonts
my personal details other than name;
Rhona Dawson
Mobile: 0491628357
NO ADDRESSES

```html
<!DOCTYPE html>
<html lang="en">
<head>
<meta charset="utf-8">
<title>R Dawson Naturopathy</title>
<link rel="stylesheet" href="https://fonts.googleapis.com/css2?family=Source+Sans+3:wght@400;600&display=swap">
<style>
  :root {
    --brand-blue: #5b9bc9;
    --sky: #66ccff;
    --mint: #a8f5e0;
    --ink: #1e1e1e;
    --field-line: #c8c8c8;
    --green-top: #a6dc3c;
    --green-bottom: #6fb41e;
    --btn-blue-top: #7fd6ff;
    --btn-blue-bottom: #1aa6f0;
    --white: #ffffff;
    --bullet: #7cc41f;
  }
  * { box-sizing: border-box; margin: 0; padding: 0; }
  html, body { width: 1027px; height: 1200px; overflow: hidden; background: var(--white); }
  body { position: relative; font-family: "Source Sans 3", sans-serif; color: var(--ink); }
  .abs { position: absolute; }

  .brand { left: 24px; top: 62px; display: flex; align-items: center; gap: 10px;
    font-size: 30px; font-weight: 400; color: var(--brand-blue); }
  .brand-dot { width: 14px; height: 14px; border-radius: 50%; background: var(--mint); }

  .phone { right: 297px; top: 42px; font-size: 23px; color: var(--brand-blue); white-space: nowrap; }
  .phone-divider { left: 740px; top: 40px; width: 1px; height: 33px; background: var(--brand-blue); }
  .appointment { left: 756px; top: 38px; width: 242px; height: 35px; border-radius: 4px;
    background: linear-gradient(var(--green-top), var(--green-bottom));
    color: var(--white); font-size: 18px; text-align: center; line-height: 34px; letter-spacing: .3px; }

  .nav a { position: absolute; top: 124px; height: 32px; line-height: 30px; font-size: 16px;
    color: var(--ink); text-decoration: none; text-align: center; }
  .nav .current { left: 429px; width: 89px; border-radius: 3px; color: var(--white);
    background: linear-gradient(var(--btn-blue-top), var(--btn-blue-bottom)); }

  .hero { left: 22px; top: 158px; width: 978px; height: 436px;
    background: linear-gradient(var(--mint), var(--sky) 75%); }
  .hero-photo { left: 15px; top: 12px; width: 950px; height: 323px;
    background: linear-gradient(90deg, #f4f7ee 0%, #e9f3d6 30%, #b9e27a 60%, #7fc93a 100%); }
  .hero-caption { left: 21px; top: 360px; width: 860px; font-size: 20px; line-height: 26px; color: var(--ink); }

  h2 { position: absolute; font-weight: 400; color: var(--brand-blue); font-size: 31px; line-height: 1; }
  .welcome-title { left: 42px; top: 609px; }
  .welcome-text { left: 44px; top: 651px; width: 580px; font-size: 14.6px; line-height: 20px; }

  .services-title { left: 42px; top: 807px; }
  .services-list { left: 48px; top: 846px; width: 258px; list-style: none; font-size: 14.5px; line-height: 20px; }
  .services-list li { position: relative; padding-left: 17px; margin-bottom: 2px; }
  .services-list li::before { content: ""; position: absolute; left: 0; top: 5px;
    border-left: 6px solid var(--bullet); border-top: 5px solid transparent; border-bottom: 5px solid transparent; }

  .rule { width: 1px; top: 818px; height: 243px; background: var(--brand-blue); }

  .contact-title { left: 342px; top: 810px; font-size: 26.5px; }
  .field { left: 343px; width: 236px; border: 1px solid var(--field-line);
    font-size: 13.5px; color: #666; padding: 3px 9px; }
  .submit { left: 499px; top: 1035px; width: 80px; height: 26px; border-radius: 3px;
    background: linear-gradient(var(--btn-blue-top), var(--btn-blue-bottom));
    font-size: 14px; text-align: center; line-height: 25px; color: var(--ink); }

  .gallery-title { left: 657px; top: 609px; }
  .thumb { width: 145px; height: 93px; }
  .more { left: 657px; top: 1016px; width: 328px; height: 23px; background: var(--brand-blue);
    color: var(--white); font-size: 14px; text-align: right; padding-right: 15px; line-height: 23px; }

  .footer { left: 22px; top: 1094px; width: 977px; height: 102px; background: var(--brand-blue);
    color: var(--white); font-size: 14px; text-align: center; padding-top: 46px; }
  .payments { margin-top: 12px; font-size: 12.5px; letter-spacing: .3px; }
</style>
</head>
<body>

<div class="abs brand"><span class="brand-dot"></span><span>R Dawson Naturopathy</span></div>

<div class="abs phone">Rhona Dawson : 0491628357</div>
<div class="abs phone-divider"></div>
<div class="abs appointment">Request an Appointment</div>

<nav class="nav">
  <a class="current" href="#">Home</a>
  <a href="#" style="left:540px;width:66px">About us</a>
  <a href="#" style="left:649px;width:62px">Services</a>
  <a href="#" style="left:752px;width:96px">Consultation</a>
  <a href="#" style="left:890px;width:80px">Contact us</a>
</nav>

<section class="abs hero">
  <div class="abs hero-photo" role="img" aria-label="Wooden mortar and pestle with herbs and flowers beside fresh green maple leaves"></div>
  <p class="abs hero-caption">Full professional iridological naturopathic diagnosis used in conjunction with the latest iris camera technology, utilising the IrisView and Lumen 5.1 software</p>
</section>

<h2 class="welcome-title">Welcome to Naturopathy</h2>
<p class="abs welcome-text">Lorem Ipsum is simply dummy text of the printing and typesetting industry. Lorem Ipsum has been the industry's standard dummy text ever since the 1500s, when an unknown printer took a galley of type and scrambled it to make a type specimen book. It has survived not only five centuries, but also the leap into electronic typesetting, remaining essentially unchanged. It was popularised in the 1960s with the release of Typeline sheets containing Lorem Ipsum passages, and more recently with desktop publishing software like Pagecraft including versions of Lorem Ipsum.</p>

<h2 class="services-title">Services</h2>
<ul class="abs services-list">
  <li>Paediatric and Adult Conditions</li>
  <li>Digestive Illness</li>
  <li>Fatigue</li>
  <li>Women’s Health</li>
  <li>Urinary conditions</li>
  <li>Nutritional advice for an evidenced-based healthy lifestyle</li>
  <li>Ear Candling</li>
  <li>Homeopathy</li>
</ul>

<div class="abs rule" style="left:311px"></div>
<div class="abs rule" style="left:605px"></div>

<h2 class="contact-title">Quick Contact</h2>
<div class="abs field" style="top:855px;height:24px">Name</div>
<div class="abs field" style="top:894px;height:24px">Email</div>
<div class="abs field" style="top:936px;height:24px">Phone</div>
<div class="abs field" style="top:974px;height:55px;padding-top:6px">Message</div>
<div class="abs submit">Submit</div>

<h2 class="gallery-title">Gallery</h2>
<div class="abs thumb" style="left:658px;top:664px;background:linear-gradient(135deg,#8a9bd8,#5a6e9e 60%,#3f5a2e)" role="img" aria-label="Blue chicory flowers"></div>
<div class="abs thumb" style="left:837px;top:664px;background:radial-gradient(circle at 50% 35%,#f2c21a 0 22%,#4f7d3a 40%,#2f4d26)" role="img" aria-label="Yellow daisy flower"></div>
<div class="abs thumb" style="left:658px;top:782px;background:radial-gradient(circle,#5f8a6a,#2f4f3a 70%,#1c2c20)" role="img" aria-label="Spiky green succulent plant"></div>
<div class="abs thumb" style="left:837px;top:782px;background:radial-gradient(circle at 50% 40%,#e0451c 0 35%,#e86fb0 60%,#f4f4f4)" role="img" aria-label="Pink echinacea coneflower"></div>
<div class="abs thumb" style="left:658px;top:903px;background:radial-gradient(circle,#5f8a6a,#2f4f3a 70%,#1c2c20)" role="img" aria-label="Spiky green succulent plant"></div>
<div class="abs more">More</div>

<footer class="abs footer">
  <p>©2012 &nbsp; - Terms of Service - Privacy Policy - Program Policies</p>
  <p class="payments">Pelo, Quintpay, Harborline Charge and TAPNET welcome</p>
</footer>

</body>
</html>
```